Billboard Vexlor-Link Systems

Design of an A0 billboard (landscape, will be printed on adhesive foil) of our company with reference to the website (www.vexlor-link.net) and the activity through keywords / phrases such as Fastest data radio you can buy, data radio safe and independent , ...
Explanation: we set up radio networks for long-range data transmission, which work on our own frequencies and are therefore independent of the provider. The systems are used for water and energy supply systems, sewage systems, environmental measurement networks, ...

Industry/Entity Type

Water-, Energie- Distribution, Abwasser...

Requirements
Must have
• Logo, link on website
Nice to have
• Message
Should not have
• picture of our old product from present web. I will be discontinued shortly. Please use the new one I uploaded here.

```html
<!DOCTYPE html>
<html lang="en">
<head>
<meta charset="utf-8">
<title>Vexlor-Link Systems – Billboard</title>
<link rel="stylesheet" href="https://fonts.googleapis.com/css2?family=Source+Sans+3:wght@300;400;700&display=swap">
<style>
  :root {
    --brand-blue: #5b87a0;
    --ink-grey: #454545;
    --paper: #ffffff;
    --photo-light: #c9c1b7;
    --photo-dark: #8a8178;
  }
  html, body {
    margin: 0;
    padding: 0;
    overflow: hidden;
    background: var(--paper);
  }
  .billboard {
    position: relative;
    width: 1200px;
    height: 848px;
    overflow: hidden;
    background: var(--paper);
    font-family: "Source Sans 3", "Helvetica Neue", Arial, sans-serif;
  }
  .backdrop {
    position: absolute;
    inset: 0;
  }
  .brand-name {
    position: absolute;
    left: 58px;
    top: 58px;
    margin: 0;
    color: var(--paper);
    font-weight: 700;
    font-size: 34px;
    line-height: 1.05;
    letter-spacing: 1px;
    text-transform: uppercase;
  }
  .headline {
    position: absolute;
    left: 60px;
    top: 262px;
    margin: 0;
    color: var(--brand-blue);
    font-weight: 700;
    font-size: 142px;
    line-height: 137px;
    letter-spacing: -1px;
  }
  .keywords {
    position: absolute;
    left: 60px;
    top: 588px;
    margin: 0;
    color: var(--ink-grey);
    font-weight: 400;
    font-size: 45px;
    letter-spacing: 0.5px;
  }
  .website {
    position: absolute;
    left: 58px;
    top: 698px;
    width: 576px;
    height: 89px;
    box-sizing: border-box;
    border: 2px solid var(--brand-blue);
    border-radius: 20px;
    display: flex;
    align-items: center;
    justify-content: center;
    color: var(--brand-blue);
    font-weight: 300;
    font-size: 58px;
    letter-spacing: 0.5px;
  }
</style>
</head>
<body>
  <main class="billboard">
    <svg class="backdrop" width="1200" height="848" viewBox="0 0 1200 848" aria-hidden="false">
      <defs>
        <linearGradient id="siteTones" x1="0" y1="0" x2="1" y2="1">
          <stop offset="0" stop-color="var(--photo-light)"/>
          <stop offset="0.6" stop-color="var(--photo-dark)"/>
          <stop offset="1" stop-color="var(--photo-light)"/>
        </linearGradient>
      </defs>
      <path class="site-photo" role="img"
            aria-label="Aerial photograph of a water treatment plant with two round clarifier basins"
            d="M340 0 C 600 110, 1000 430, 1200 750 L1200 0 Z"
            fill="url(#siteTones)"/>
      <path class="brand-band"
            d="M0 0 L1200 0 C 900 40, 300 150, 0 266 Z"
            fill="var(--brand-blue)" fill-opacity="0.92"/>
    </svg>

    <p class="brand-name">Vexlor-Link<br>Systems</p>

    <h1 class="headline">Data radio<br>you can buy</h1>

    <p class="keywords">SAFE | FAST | INDEPENDENT</p>

    <div class="website">www.vexlor-link.net</div>
  </main>
</body>
</html>
```